Preisliste für Kosmetikinstitut
Zielgruppe
Ich benötige für mein Kosmetikinstitut eine Preisliste für die moderne Frau, aber auch Männer. Das Design sollte mein Logo enthalten. Farben des Designkonzepts einbauen.
A4 quer zum Falten, wie ein Heft, 1. Seite Preisliste mit logo, im Innenteil dann Anwendungen
Aufgabenstellung
Minimalistisch, ästhetisch, modern, edel
Kontaktdaten auf der Rückseite
LT Hautatelier
Lena Tessmar
Lindenstieg 17
83671 Ostermoor
EMail: lena@lt-hautatelier.de
Whatsapp: 0176 284 9017

```html
<!DOCTYPE html>
<html lang="de">
<head>
<meta charset="utf-8">
<title>Preisliste – LT Hautatelier</title>
<link rel="stylesheet" href="https://fonts.googleapis.com/css2?family=Alegreya+Sans:wght@400;500;700&family=Cormorant+Garamond:wght@300;400&display=swap">
<style>
  :root {
    --backdrop: #d5d5d5;
    --paper: #e4e3e1;
    --paper-light: #eceae8;
    --frame: #f7f7f6;
    --ink: #5e6465;
    --ink-soft: #7a7f80;
    --texture-a: #dcdcdc;
    --texture-b: #c9c9ca;
    --skin-a: #c9a48e;
    --skin-b: #a7a9ac;
  }
  * { box-sizing: border-box; margin: 0; padding: 0; }
  html, body { width: 1200px; height: 800px; overflow: hidden; }
  body {
    background: var(--backdrop);
    font-family: "Alegreya Sans", sans-serif;
    color: var(--ink);
    position: relative;
  }
  .page {
    position: absolute;
    top: 152px;
    width: 350px;
    height: 495px;
    background: var(--paper);
    overflow: hidden;
  }

  /* Cover */
  .cover { left: 55px; }
  .cover__texture {
    position: absolute;
    left: 20%; top: 8%;
    width: 42%; height: 52%;
    background: linear-gradient(150deg, var(--texture-a) 0%, var(--texture-b) 45%, var(--texture-a) 70%, var(--texture-b) 100%);
  }
  .cover__brand {
    position: absolute;
    left: 20%; top: 8%;
    width: 42%; height: 52%;
    display: flex; align-items: center; justify-content: center;
    font-family: "Alegreya Sans", sans-serif;
    font-weight: 400;
    font-size: 15px;
    letter-spacing: 0.06em;
    color: var(--ink-soft);
  }
  .cover__title {
    position: absolute;
    left: 0; right: 0; bottom: 14%;
    text-align: center;
    padding-left: 40px;
    font-family: "Cormorant Garamond", serif;
    font-weight: 300;
    font-size: 26px;
    letter-spacing: 0.32em;
    color: var(--ink-soft);
  }

  /* Inner spread */
  .inner-left {
    left: 445px;
    background: var(--frame);
    padding: 12px;
  }
  .inner-left__panel {
    width: 100%; height: 100%;
    background: var(--paper-light);
    padding: 50px 28px 0 34px;
  }
  .inner-right { left: 795px; }
  .inner-right__content { padding: 26px 40px 0 38px; }
  .inner-right .treatment { margin-bottom: 14px; }
  .inner-right .treatment__text { line-height: 1.4; }

  .section-title {
    font-weight: 700;
    font-size: 12px;
    letter-spacing: 0.1em;
    text-transform: uppercase;
    margin-bottom: 22px;
  }
  .treatment { margin-bottom: 20px; }
  .treatment__head {
    display: flex; justify-content: space-between; align-items: baseline;
    font-weight: 700;
    font-size: 11px;
    letter-spacing: 0.07em;
    text-transform: uppercase;
  }
  .treatment__sub {
    font-weight: 700;
    font-size: 11px;
    letter-spacing: 0.07em;
    text-transform: uppercase;
  }
  .treatment__price {
    font-weight: 700;
    letter-spacing: 0.03em;
    white-space: nowrap;
    margin-left: 12px;
  }
  .treatment__text {
    margin-top: 3px;
    font-size: 10.5px;
    line-height: 1.45;
    color: var(--ink-soft);
  }

  .photo {
    position: absolute;
    bottom: 0;
  }
  .photo--one {
    left: 0; width: 40%; top: 73%;
    background: linear-gradient(120deg, var(--skin-b) 0%, var(--skin-a) 60%, #b8927c 100%);
  }
  .photo--two {
    left: 41%; width: 32%; top: 78%;
    background: linear-gradient(140deg, var(--skin-a) 0%, #b9b9bb 100%);
  }
</style>
</head>
<body>

  <section class="page cover">
    <div class="cover__texture" role="img" aria-label="Helle, seidig fließende Textur in Grautönen"></div>
    <div class="cover__brand">LT Hautatelier</div>
    <h1 class="cover__title">PREISLISTE</h1>
  </section>

  <section class="page inner-left">
    <div class="inner-left__panel">
      <h2 class="section-title">Gesichtsbehandlungen</h2>

      <article class="treatment">
        <div class="treatment__head"><span>Basic Treatment</span><span class="treatment__price">€ 59,00</span></div>
        <p class="treatment__text">Für alle, die wenig Zeit haben und trotzdem ihre Haut pflegen und verwöhnen wollen. Reinigung, Peeling, Maske, ca. 45min</p>
      </article>

      <article class="treatment">
        <div class="treatment__head"><span>Classic Treatment</span><span class="treatment__price">€ 89,00</span></div>
        <div class="treatment__sub">Klassische Behandlung</div>
        <p class="treatment__text">Reinigung, Peeling, Ausreinigung, Massage, Wirkstoffpflege, individuelle Maske. ca. 75min</p>
      </article>

      <article class="treatment">
        <div class="treatment__head"><span>Hydra Boost</span><span class="treatment__price">€ 89,00</span></div>
        <p class="treatment__text">Trockene Haut wird intensiv mit Feuchtigkeit versorgt, die Haut kann sich regenerieren und die Tiefe der Fältchen wird gemildert. ca. 60min</p>
      </article>

      <article class="treatment">
        <div class="treatment__head"><span>Pure Skin</span><span class="treatment__price">€ 79,00</span></div>
        <p class="treatment__text">Unreine Haut wird ausgeglichen, Poren verfeinert und Rötungen beruhigt. ca. 60min</p>
      </article>
    </div>
  </section>

  <section class="page inner-right">
    <div class="inner-right__content">
      <article class="treatment">
        <div class="treatment__head"><span>Calmira Soft Treatment</span><span class="treatment__price">€ 79,00</span></div>
        <div class="treatment__sub">(Für die empfindliche, gereizte Haut)</div>
        <p class="treatment__text">Entzündliche Prozesse können gemildert werden, gereizte Haut oder solche, die wenig verträgt, wird beruhigt. Irritationen können zurückgehen, die Haut erhält Balance. ca. 50min</p>
      </article>

      <article class="treatment">
        <div class="treatment__head"><span>Vitamin Soft Boost</span><span class="treatment__price">€ 79,00</span></div>
        <p class="treatment__text">Vitamine sorgen für Power und Frische in und auf der Haut, die Widerstandskraft der Haut wird gestärkt. Die Faltentiefe kann gemildert werden. ca. 50min</p>
      </article>

      <article class="treatment">
        <div class="treatment__head"><span>Anti-Age Advanced</span><span class="treatment__price">€ 99,00</span></div>
        <p class="treatment__text">Die Haut wirkt insgesamt erfrischt, vitalisiert und gestrafft. Feine Linien und Fältchen werden reduziert. 50–70min (je nach Peeling)</p>
      </article>

      <article class="treatment">
        <div class="treatment__head"><span>Chemisches Peeling</span><span class="treatment__price">€ 89,00</span></div>
        <div class="treatment__sub">(Oktober – April)</div>
        <p class="treatment__text">Professionelle Peelings können viele Problemstellungen lindern, verbessern oder gar beheben. Dazu gehören die Zellerneuerung, Glättung der Hauttextur, Reduzierung von Pigmentflecken, Verbesserung von Akne</p>
      </article>
    </div>
    <div class="photo photo--one" role="img" aria-label="Porträtfoto einer Frau mit gepflegter Haut, linke Gesichtshälfte"></div>
    <div class="photo photo--two" role="img" aria-label="Porträtfoto einer Frau mit gepflegter Haut, rechte Gesichtshälfte"></div>
  </section>

</body>
</html>
```